Accountability Project Graphics

I want to create 10 social media graphics (new Instagram size 4:5 (1080 x 1350 pixels) focusing on our Kelmora Accountability App, using any of the 3 pictures attached. Use the attached pics only, NO RANDOM STOCK PHOTOGRAPHY. For the color scheme, use the landing page colors/fonts (attached).
You can add any of the 3 photos attached but I mainly need BOLD text that includes these headlines and sub-headlines on them.
Please NOTE for all the headlines below, also add this sub-headline on each graphic:
Stay Consistent with MB in Your Pocket!
Here are the headlines:
• Stop Starting Over Every Monday
• You don't need more willpower. You need more support
• Built for women who are tired of doing this alone
• When Motivation Fades, MB Checks In
• The Support System You've Been Missing
• Support When Motivation Disappears
• What if MB Checked in Every Day?
• The Missing Piece Isn't Another Diet
• Eat the food you love. Stay accountable every day.
• One Bad Meal Doesn't Mean You Failed
women over 40 trying to lose weight

```html
<!DOCTYPE html>
<html lang="en">
<head>
<meta charset="utf-8">
<title>Kelmora Accountability App – Social Graphics</title>
<link rel="stylesheet" href="https://fonts.googleapis.com/css2?family=Montserrat:wght@400;500;700;800;900&family=Oswald:wght@500;600&family=Nunito:wght@400;600&family=Great+Vibes&family=Allura&display=swap">
<style>
  :root{
    --canvas:#faf9f7;
    --pink:#e0578e;
    --pink-deep:#c3386f;
    --pink-soft:#f07aab;
    --magenta:#e05bc9;
    --lavender:#d8b3ef;
    --yellow:#f6cf4e;
    --blue:#6ea2c2;
    --teal:#3ba2a8;
    --white:#ffffff;
    --ink:#4a4a4a;
    --navy:#23283d;
  }
  *{margin:0;padding:0;box-sizing:border-box}
  html,body{width:1192px;height:1200px;overflow:hidden;background:var(--canvas)}
  .board{position:relative;width:1192px;height:1200px}
  .card{position:absolute;width:262px;height:328px;overflow:hidden;box-shadow:0 8px 12px rgba(0,0,0,.18)}
  .card > *{position:absolute}
  .photo{background:linear-gradient(160deg,rgba(120,70,60,.55) 0%,var(--navy) 55%,#1b1e2e 100%)}
  .photo--duo{background:linear-gradient(150deg,#2a2f46 0%,#7b5648 45%,#f0e6ee 100%)}
  .photo--hug{background:linear-gradient(135deg,#2b2a55 0%,#6a3b4a 40%,#d9547f 70%,#f4eef2 100%)}
  .decor{opacity:.55}
  .sans{font-family:"Montserrat",sans-serif}
  .cond{font-family:"Oswald",sans-serif;font-weight:600;line-height:1.1;text-transform:uppercase}
  .script{font-family:"Great Vibes",cursive;line-height:1}
  .tagline{font-family:"Nunito",sans-serif;font-size:11px;color:var(--white);white-space:nowrap}
  .band{left:0;width:100%;height:18px;display:flex;align-items:center;justify-content:center}
  .bold{font-family:"Montserrat",sans-serif;font-weight:800;line-height:.95;text-transform:uppercase}

  /* card 1 */
  .c-monday{background:linear-gradient(180deg,#efdcf7 0%,var(--lavender) 55%,#cf73d9 100%)}
  .c-monday .word{color:var(--magenta)}
  .c-monday .vert{writing-mode:vertical-rl;transform:rotate(180deg)}
  /* card 2 */
  .c-willpower{background:var(--pink-soft)}
  /* card 3 */
  .c-alone{background:var(--pink)}
  /* card 4 */
  .c-fades{background:var(--blue)}
  /* card 5 */
  .c-system{background:linear-gradient(180deg,var(--pink-soft) 0%,#f5a6c6 60%,#f3f1f2 85%)}
  /* card 6 */
  .c-disappears{background:var(--pink-soft)}
  /* card 7-9 */
  .c-checked,.c-diet,.c-eat{background:var(--pink)}
  /* card 10 */
  .c-failed{background:var(--teal)}
</style>
</head>
<body>
<main class="board">

  <!-- Stop Starting Over Every Monday -->
  <section class="card c-monday" style="left:323px;top:70px">
    <div class="decor" role="img" aria-label="Watercolour flower bouquet" style="left:170px;top:20px;width:92px;height:110px;border-radius:50%;background:radial-gradient(circle,#f3c4d6,#c9b4e4 60%,transparent 72%)"></div>
    <div class="photo" role="img" aria-label="Coach smiling with hand on hip, black lace top" style="left:90px;top:68px;width:172px;height:260px;border-radius:70px 70px 0 0"></div>
    <div class="bold word" style="left:16px;top:14px;font-size:58px;font-weight:900">STOP</div>
    <div class="sans word vert" style="left:14px;top:70px;height:135px;font-size:27px;font-weight:500;text-align:left">STARTING</div>
    <div class="bold word vert" style="left:40px;top:66px;height:140px;font-size:48px;text-align:left">OVER</div>
    <div class="sans word" style="left:15px;top:207px;font-size:23px;font-weight:500">EVERY</div>
    <div class="bold word" style="left:14px;top:232px;font-size:40px">MONDAY</div>
    <div class="tagline" style="left:30px;top:302px">Stay Consistent with MB in Your Pocket!</div>
  </section>

  <!-- You don't need more willpower -->
  <section class="card c-willpower" style="left:607px;top:70px">
    <div class="photo--hug" role="img" aria-label="Coach hugging a client and laughing" style="left:60px;top:45px;width:202px;height:283px"></div>
    <div style="left:0;top:250px;width:262px;height:78px;background:linear-gradient(180deg,transparent,#f6f3f4 70%)"></div>
    <div class="sans" style="left:17px;top:14px;font-size:12px;color:var(--white)">YOU DON'T NEED MORE</div>
    <div class="script" style="left:20px;top:32px;font-size:28px;color:var(--yellow)">willpower</div>
    <div class="bold" style="left:16px;top:178px;font-size:31px;color:var(--pink)">YOU<br>NEED<br>MORE<br>SUPPORT</div>
    <div class="tagline" style="left:17px;top:304px;color:var(--ink);font-size:10px">Stay Consistent with MB in Your Pocket!</div>
  </section>

  <!-- Built for women -->
  <section class="card c-alone" style="left:40px;top:431px">
    <div class="photo" role="img" aria-label="Coach smiling with hand on hip" style="left:0;top:20px;width:175px;height:308px;border-radius:0 80px 0 0"></div>
    <div class="bold" style="left:108px;top:58px;font-size:42px;color:var(--white)">BUILT</div>
    <div class="script" style="left:100px;top:100px;font-size:30px;color:var(--white)">for women</div>
    <div class="bold" style="left:108px;top:133px;font-size:27px;color:var(--yellow)">WHO ARE</div>
    <div class="bold" style="left:108px;top:163px;font-size:14px;color:var(--white)">TIRED OF DOING</div>
    <div class="script" style="left:104px;top:180px;font-size:30px;color:var(--white)">this</div>
    <div class="bold" style="left:102px;top:210px;font-size:37px;color:var(--yellow)">ALONE</div>
    <div class="tagline" style="left:17px;top:301px">Stay Consistent with MB in Your Pocket!</div>
  </section>

  <!-- When motivation fades -->
  <section class="card c-fades" style="left:322px;top:431px">
    <div class="photo--duo" role="img" aria-label="Coach and client standing together laughing" style="left:0;top:120px;width:262px;height:208px"></div>
    <div class="sans" style="left:17px;top:13px;font-size:19px;font-weight:600;color:var(--white)">WHEN</div>
    <div class="bold" style="left:18px;top:37px;font-size:31px;color:var(--yellow)">MOTIVATION</div>
    <div class="sans" style="right:20px;top:68px;font-size:24px;font-weight:500;color:var(--white)">FADES</div>
    <svg style="left:178px;top:95px" width="80" height="24" viewBox="0 0 80 24"><ellipse cx="40" cy="12" rx="38" ry="10" fill="none" stroke="#fff" stroke-width="1"/></svg>
    <div class="sans" style="left:184px;top:101px;font-size:9px;font-weight:600;color:var(--white)">MB CHECKS IN</div>
    <div class="band" style="top:301px;background:#3d86ad"><span class="tagline" style="font-size:12px">Stay Consistent with MB in Your Pocket!</span></div>
  </section>

  <!-- The support system -->
  <section class="card c-system" style="left:605px;top:431px">
    <div class="photo--hug" role="img" aria-label="Coach hugging a client and laughing" style="left:0;top:45px;width:205px;height:215px;opacity:.9"></div>
    <div class="sans" style="left:50px;top:14px;font-size:22px;font-weight:500;letter-spacing:3px;color:var(--white)">THE SUPPORT</div>
    <div class="sans" style="left:211px;top:48px;writing-mode:vertical-rl;font-size:42px;font-weight:500;letter-spacing:2px;color:var(--white)">SYSTEM</div>
    <div class="sans" style="right:16px;top:252px;font-size:12px;color:var(--ink)">YOU'VE BEEN</div>
    <div class="script" style="right:16px;top:262px;font-size:38px;color:var(--pink)">Missing</div>
    <div class="tagline" style="left:18px;top:305px;color:var(--ink);font-size:9px;letter-spacing:1px">STAY CONSISTENT WITH MB IN YOUR POCKET!</div>
  </section>

  <!-- Support when motivation disappears -->
  <section class="card c-disappears" style="left:888px;top:431px">
    <div class="photo--hug" role="img" aria-label="Coach hugging a client and laughing" style="left:20px;top:140px;width:242px;height:188px"></div>
    <div class="script" style="left:22px;top:12px;font-size:42px;color:var(--white)">Support</div>
    <div class="sans" style="left:157px;top:45px;font-size:22px;font-weight:500;color:var(--white)">WHEN</div>
    <div class="sans" style="left:18px;top:68px;font-size:31px;font-weight:500;color:var(--white)">MOTIVATION</div>
    <div class="sans" style="right:20px;top:106px;font-size:19px;color:var(--white)">Disappears</div>
    <div class="band" style="top:298px;background:var(--pink-deep)"><span class="tagline">Stay Consistent with MB in Your Pocket!</span></div>
  </section>

  <!-- What if MB checked in -->
  <section class="card c-checked" style="left:41px;top:795px">
    <div class="photo" role="img" aria-label="Coach smiling with hand on hip, pink petals behind" style="left:108px;top:0;width:154px;height:328px;border-radius:70px 0 0 0"></div>
    <div class="cond" style="left:18px;top:62px;font-size:38px;color:var(--white)">WHAT IF</div>
    <div class="script" style="left:48px;top:106px;font-size:36px;color:var(--white)">MB</div>
    <div style="left:0;top:148px;width:168px;height:44px;background:#e7c04a"></div>
    <div class="cond" style="left:18px;top:148px;font-size:38px;color:var(--white)">CHECKED<br>IN EVERY<br>DAY?</div>
    <div class="tagline" style="left:17px;top:302px">Stay Consistent with MB in Your Pocket!</div>
  </section>

  <!-- Missing piece isn't another diet -->
  <section class="card c-diet" style="left:323px;top:795px">
    <div class="photo--duo" role="img" aria-label="Coach and client standing together laughing" style="left:40px;top:195px;width:200px;height:133px"></div>
    <div class="script" style="left:0;width:100%;text-align:center;top:20px;font-size:30px;color:var(--white)">The Missing</div>
    <div class="sans" style="left:0;width:100%;text-align:center;top:56px;font-size:28px;font-weight:400;color:var(--white)">PIECE ISN'T</div>
    <div class="bold" style="left:0;width:100%;text-align:center;top:92px;font-size:37px;color:var(--white)">ANOTHER</div>
    <div class="bold" style="left:0;width:100%;text-align:center;top:132px;font-size:86px;font-weight:900;color:#f2f2f2">DIET</div>
    <div class="band" style="top:298px;background:var(--pink-deep)"><span class="tagline">Stay Consistent with MB in Your Pocket!</span></div>
  </section>

  <!-- Eat the food you love -->
  <section class="card c-eat" style="left:603px;top:795px">
    <div class="photo" role="img" aria-label="Coach smiling with hand on hip, pink petals behind" style="left:110px;top:0;width:152px;height:328px;border-radius:70px 0 0 0"></div>
    <div class="cond" style="left:17px;top:20px;font-size:42px;line-height:1.13;color:var(--white)">EAT<br>THE<br>FOOD<br>YOU<br>LOVE</div>
    <div class="cond" style="left:18px;top:260px;font-size:13px;line-height:1.05;color:var(--white)">STAY ACCOUNTABLE<br>EVERY DAY</div>
    <div class="tagline" style="left:17px;top:302px">Stay Consistent with MB in Your Pocket!</div>
  </section>

  <!-- One bad meal -->
  <section class="card c-failed" style="left:888px;top:795px">
    <div class="photo" role="img" aria-label="Coach smiling with hand on hip, teal leaves behind" style="left:115px;top:0;width:147px;height:328px;border-radius:70px 0 0 0"></div>
    <div style="left:2px;top:130px;width:138px;height:44px;background:#e7c04a;border-radius:4px 14px 8px 16px"></div>
    <div class="cond" style="left:17px;top:52px;font-size:36px;line-height:1.08;color:var(--white)">ONE BAD<br>MEAL<br>DOESN'T<br>MEAN<br>YOU<br>FAILED</div>
    <div class="tagline" style="left:17px;top:303px">Stay Consistent with MB in Your Pocket!</div>
  </section>

</main>
</body>
</html>
```